Kitchen and bathroom exhaust fan cleaning business card design

A new business cleaning domestic - not commercial - exhaust/extractor fans in kitchens, bathrooms and en suites and kitchen range hood filters.

We would like a bright colour suggesting cleanliness (such a syellow or light green?)

I would like to see on the card preferably on the reverse:

"We clean kitchen and bathroom exhaust fans & Volrex Brightos
and
clean and repair range hood filters and replace carbon filters

We give Pensioner discounts
Updates

Designers pls note the TM in the contact filed after Pureflow Vents should be superscript as in the trademark sign. On the reverse of the card, I would like:: "We clean kitchen and bathroom exhaust fans & Volrex Brightos & clean and repair range hood filters and replace carbon filters We give Pensioner discounts

Reason: I will be out of the country for several days

Target Market(s)

people who are too lazy or too busy to clean their fan units and pensioners and others who are unable to do it.

Industry/Entity Type

Business

Contact Information for Business Card

ACT Clean FansTM Designer pls note the TM should be superscript as in the trademark sign
Neil Oakley
Mob: 0431 572 864
Email: pureflowvents@zentromail.com
PO Box 7152, Pellow ACT 2608

Requirements
Must have
• Designer pls note the TM in the contact filed after Pureflow Vents should be superscript as in the trademark sign.

On the reverse

and

```html
<!DOCTYPE html>
<html lang="en">
<head>
<meta charset="utf-8">
<title>Pureflow Vents – Business Card</title>
<link rel="stylesheet" href="https://fonts.googleapis.com/css2?family=Exo+2:wght@400;600&display=swap">
<style>
  :root {
    --backdrop: #e4e5e7;
    --card: #ffffff;
    --ink: #2e2f31;
    --band: #343537;
    --accent: #16a9ec;
    --muted: #55575a;
    --on-band: #ffffff;
  }
  * { margin: 0; padding: 0; box-sizing: border-box; }
  html, body {
    width: 1200px; height: 854px; overflow: hidden;
    background: var(--backdrop);
    font-family: "Exo 2", "Segoe UI", sans-serif;
  }
  .card {
    position: absolute; top: 112px;
    width: 360px; height: 630px;
    background: var(--card);
    overflow: hidden;
    box-shadow: 0 8px 24px rgba(0,0,0,0.12);
  }
  .card-back { left: 190px; }
  .card-front { left: 650px; }
  .card-art { position: absolute; left: 0; top: 0; width: 360px; height: 630px; }

  /* Reverse side */
  .back-brand {
    position: absolute; left: 0; right: 0; top: 150px;
    text-align: center; color: var(--ink);
    font-weight: 600; font-size: 38px; line-height: 1.05;
  }
  .back-brand sup, .brand sup { font-size: 13px; vertical-align: super; }
  .back-rule {
    position: absolute; left: 150px; top: 262px;
    width: 60px; height: 4px; border-radius: 2px; background: var(--accent);
  }
  .services {
    position: absolute; left: 40px; right: 40px; top: 296px;
    text-align: center; color: var(--muted);
    font-size: 17px; line-height: 1.5;
  }
  .discount {
    position: absolute; left: 40px; right: 40px; top: 470px;
    text-align: center; color: var(--accent);
    font-weight: 600; font-size: 19px; letter-spacing: 0.5px;
  }

  /* Front side */
  .brand {
    position: absolute; right: 40px; top: 50px;
    text-align: right; color: var(--ink);
    font-weight: 600; font-size: 34px; line-height: 1.05;
  }
  .person { position: absolute; left: 40px; top: 180px; }
  .person-name { color: var(--ink); font-weight: 600; font-size: 28px; letter-spacing: 1px; }
  .person-role { color: var(--accent); font-size: 13px; letter-spacing: 1.5px; margin-top: 2px; }
  .contact-list {
    position: absolute; left: 40px; top: 262px;
    list-style: none; color: var(--muted); font-size: 14px; letter-spacing: 0.4px;
  }
  .contact-list li { display: flex; align-items: center; gap: 9px; height: 24px; }
  .contact-list li.gap { margin-top: 14px; }
  .contact-icon { width: 15px; height: 15px; flex: none; }
  .address {
    position: absolute; left: 40px; top: 474px;
    color: var(--on-band); font-size: 23px; line-height: 1.35; letter-spacing: 0.5px;
  }
</style>
</head>
<body>
  <section class="card card-back" aria-label="Card reverse">
    <svg class="card-art" viewBox="0 0 360 630" aria-hidden="true">
      <rect x="16" y="16" width="328" height="14" rx="7" fill="var(--band)"/>
      <rect x="16" y="600" width="328" height="14" rx="7" fill="var(--band)"/>
    </svg>
    <div class="back-brand">Pureflow<br>Vents<sup>TM</sup></div>
    <div class="back-rule"></div>
    <p class="services">We clean kitchen and bathroom exhaust fans &amp; Volrex Brightos &amp; clean and repair range hood filters and replace carbon filters</p>
    <p class="discount">We give Pensioner discounts</p>
  </section>

  <section class="card card-front" aria-label="Card front">
    <svg class="card-art" viewBox="0 0 360 630" aria-hidden="true">
      <path d="M0 432 Q180 360 360 432 L360 630 L0 630 Z" fill="var(--band)"/>
      <rect x="16" y="576" width="328" height="22" rx="7" fill="var(--accent)"/>
    </svg>

    <div class="brand">Pureflow<br>Vents<sup>TM</sup></div>

    <div class="person">
      <div class="person-name">NEIL OAKLEY</div>
      <div class="person-role">GENERAL MANAGER</div>
    </div>

    <ul class="contact-list">
      <li>
        <svg class="contact-icon" viewBox="0 0 16 16"><circle cx="8" cy="8" r="8" fill="var(--accent)"/><path d="M5.2 4.2l1.6 1.6-.9 1.2a5 5 0 0 0 3.1 3.1l1.2-.9 1.6 1.6-1.3 1.2C7.6 12 4 8.4 4 5.5z" fill="#fff"/></svg>
        0431 572 864
      </li>
      <li>
        <svg class="contact-icon" viewBox="0 0 16 16"><circle cx="8" cy="8" r="8" fill="var(--accent)"/><rect x="5.5" y="3.5" width="5" height="9" rx="1" fill="#fff"/></svg>
        0431 572 865
      </li>
      <li class="gap">
        <svg class="contact-icon" viewBox="0 0 16 16"><circle cx="8" cy="8" r="8" fill="var(--accent)"/><rect x="4" y="5" width="8" height="6" fill="#fff"/><path d="M4 5l4 3.2L12 5" stroke="var(--accent)" fill="none"/></svg>
        pureflowvents@zentromail.com
      </li>
      <li>
        <svg class="contact-icon" viewBox="0 0 16 16"><circle cx="8" cy="8" r="8" fill="var(--accent)"/><circle cx="8" cy="8" r="4" fill="none" stroke="#fff" stroke-width="1.2"/><path d="M4 8h8M8 4v8" stroke="#fff" stroke-width="1"/></svg>
        www.pureflowvents.com.au
      </li>
    </ul>

    <div class="address">PO Box 7152,<br>Pellow ACT 2608</div>
  </section>
</body>
</html>
```